CraneHollow - Business Card and Letterhead

After having received some fantastic submissions in our recent logo design project, I would now like to extend our branding to letterheads and business cards.
CraneHollow is a consulting service in the Construction Industry. We deal with both residential and commercial projects, and our clients include Architects, Builders, Tradespeople and Home Owners.
The designs should be simple and effective, convey personal service and professionalism, and display some level of creativity.
For both the business cards and letterhead, a white card stock will be used. This project is for business cards and letterheads only. Our new logo is attached for use.
The designs should incorporate our two main colours which are Blue (RGB 14,92,143) and Green (RGB 132,194,37).
For the time being, please submit all designs showing generic information including name, mobile number, email, postal address and website details. No fax number or physical address is required. I will provide our actual contact details once a final design has been selected.
I encourage you to interpret this brief in your own creative way, and look forward to some quality submissions.
Thanks!
Leo
CraneHollow.

```html
<!DOCTYPE html>
<html lang="en">
<head>
<meta charset="utf-8">
<title>CraneHollow – Letterhead and Business Cards</title>
<link href="https://fonts.googleapis.com/css2?family=Questrial&family=Montserrat:wght@600&display=swap" rel="stylesheet">
<style>
  :root {
    --blue: #0e5c8f;
    --blue-deep: #164f7a;
    --green: #84c225;
    --green-soft: #dfeccb;
    --slate: #6e8ca6;
    --ink: #4a4a4a;
    --ink-soft: #777;
    --panel: #ececec;
    --row-alt: #f1f1f1;
    --page: #ffffff;
    --backdrop: #ebebeb;
  }
  * { box-sizing: border-box; margin: 0; padding: 0; }
  html, body {
    width: 1200px; height: 979px; overflow: hidden;
    background: var(--backdrop);
    font-family: "Questrial", "Century Gothic", sans-serif;
    color: var(--ink);
  }
  address { font-style: normal; }
  .letterhead {
    position: absolute; left: 48px; top: 50px;
    width: 620px; height: 877px;
    background: var(--page);
    box-shadow: 0 2px 10px rgba(0,0,0,.12);
  }
  .sender-address {
    position: absolute; right: 48px; top: 44px;
    text-align: right; font-size: 9px; line-height: 1.5; color: var(--ink-soft);
  }
  .sender-address .web { color: var(--blue); }
  .brand { display: flex; align-items: center; gap: 8px; }
  .brand-square { background: var(--green); }
  .brand-name { color: var(--blue); }
  .letterhead .brand { position: absolute; left: 48px; top: 150px; }
  .letterhead .brand-square { width: 20px; height: 20px; }
  .letterhead .brand-name { font-size: 27px; }

  .invoice-details {
    position: absolute; left: 48px; top: 238px;
    width: 192px; height: auto;
    background: var(--panel);
    padding: 18px 20px 22px;
    font-size: 9.5px; line-height: 1.5; color: var(--ink-soft);
  }
  .invoice-details h2 { font-weight: 400; font-size: 15px; color: var(--ink); margin-bottom: 10px; }
  .invoice-details p + p { margin-top: 8px; }

  .invoice-body { position: absolute; left: 266px; top: 206px; width: 306px; }
  .invoice-body h1 { font-weight: 400; font-size: 16px; color: var(--ink); margin-bottom: 8px; }
  .invoice-body .intro { font-size: 9px; line-height: 1.5; color: var(--ink-soft); margin-bottom: 12px; }
  .services { width: 100%; border-collapse: collapse; font-size: 8.5px; }
  .services th {
    background: var(--slate); color: #fff; font-weight: 400;
    text-align: left; padding: 7px 6px; height: 26px;
  }
  .services td { padding: 0 6px; height: 22px; color: var(--ink-soft); }
  .services tbody tr:nth-child(even) td { background: var(--row-alt); }
  .services .num, .services th.num { text-align: right; }
  .services tfoot td { background: var(--slate); color: #fff; height: 24px; }
  .questions { margin-top: 14px; font-size: 9px; line-height: 1.6; color: var(--ink-soft); }
  .questions strong { font-weight: 400; color: var(--ink); display: block; }

  .edge-bands { position: absolute; left: 0; bottom: 0; width: 100%; height: 70px; display: block; }

  .card {
    position: absolute; width: 420px; height: 240px;
    box-shadow: 0 2px 10px rgba(0,0,0,.12);
    overflow: hidden;
  }
  .card-front { left: 724px; top: 130px; background: var(--page); }
  .card-front .brand { position: absolute; left: 30px; top: 34px; }
  .card-front .brand-square { width: 16px; height: 16px; }
  .card-front .brand-name { font-size: 22px; }
  .card-holder {
    position: absolute; right: 30px; top: 84px;
    font-family: "Montserrat", sans-serif; font-weight: 600;
    font-size: 12px; letter-spacing: .06em; color: var(--ink);
  }
  .card-contact {
    position: absolute; left: 30px; top: 126px;
    font-size: 9px; line-height: 1.55; color: var(--ink-soft);
  }
  .card-contact b { font-weight: 400; color: var(--blue); }
  .card-front .edge-bands { height: 70px; }

  .card-back {
    left: 724px; top: 440px;
    background: radial-gradient(ellipse at 35% 40%, #2a78ad 0%, var(--blue) 55%, var(--blue-deep) 100%);
    display: flex; align-items: center; justify-content: center;
  }
  .card-back .brand-square { width: 18px; height: 18px; }
  .card-back .brand-name { color: #fff; font-size: 24px; }
</style>
</head>
<body>

<article class="letterhead">
  <address class="sender-address">
    18 Ridgeline Road, Avoca NSW 2251<br>
    www.<span class="web">cranehollow.com</span>
  </address>

  <div class="brand">
    <span class="brand-square"></span>
    <span class="brand-name">CraneHollow</span>
  </div>

  <section class="invoice-details">
    <h2>Invoice</h2>
    <p>41 Quarry Lane<br>Suite 12<br>Fernvale, QLD 4306</p>
    <p>Phone / 07 5550 1842<br>Email /<br>fernvaleworks.com<br>Fax / 07 5550 2976<br>Web /<br>fernvalebuild.com<br>Date / July 4, 2009<br>To / Mr Tom Ashby<br>From / Your Name</p>
  </section>

  <section class="invoice-body">
    <h1>Thank You for Your Business!</h1>
    <p class="intro">Every project we guide is built on clear advice, careful planning and honest costs. We appreciate your trust and look forward to working with you again on future builds.</p>
    <table class="services">
      <thead>
        <tr><th>Service Rendered</th><th class="num">Cost</th><th class="num">Date</th></tr>
      </thead>
      <tbody>
        <tr><td>Site assessment and report</td><td class="num">$000</td><td class="num">01/01/11</td></tr>
        <tr><td>Planning review with architect</td><td class="num">$000</td><td class="num">01/01/11</td></tr>
        <tr><td>Budget and cost estimate</td><td class="num">$000</td><td class="num">01/01/11</td></tr>
        <tr><td>Builder tender review meeting</td><td class="num">$000</td><td class="num">01/01/11</td></tr>
        <tr><td>Council approval lodgement support</td><td class="num">$000</td><td class="num">01/01/11</td></tr>
        <tr><td>Trade schedule and timeline</td><td class="num">$000</td><td class="num">01/01/11</td></tr>
        <tr><td>Weekly site progress visit</td><td class="num">$000</td><td class="num">01/01/11</td></tr>
        <tr><td>Materials selection advice session</td><td class="num">$000</td><td class="num">01/01/11</td></tr>
        <tr><td>Variation review and notes</td><td class="num">$000</td><td class="num">01/01/11</td></tr>
        <tr><td>Final handover inspection report</td><td class="num">$000</td><td class="num">01/01/11</td></tr>
      </tbody>
      <tfoot>
        <tr><td>Total</td><td class="num">$10,182</td><td class="num">12/01/11</td></tr>
      </tfoot>
    </table>
    <p class="questions"><strong>Questions?</strong>Call us any time and we will gladly help.</p>
  </section>

  <svg class="edge-bands" viewBox="0 0 620 70" preserveAspectRatio="none" aria-hidden="true">
    <polygon points="400,8 620,8 620,70 384,70" fill="var(--green-soft)"/>
    <polygon points="400,8 620,8 620,22 397,22" fill="var(--green)"/>
    <polygon points="0,54 388,54 386,64 0,64" fill="var(--blue)"/>
  </svg>
</article>

<article class="card card-front">
  <div class="brand">
    <span class="brand-square"></span>
    <span class="brand-name">CraneHollow</span>
  </div>
  <p class="card-holder">NORA WHITFIELD</p>
  <address class="card-contact">
    18 Ridgeline Road, Avoca NSW 2251<br>
    <b>M:</b> 0412 555 390 &nbsp;<b>E:</b> nora@cranehollow.com<br>
    www.cranehollow.com
  </address>
  <svg class="edge-bands" viewBox="0 0 420 70" preserveAspectRatio="none" aria-hidden="true">
    <polygon points="270,6 420,6 420,70 258,70" fill="var(--green-soft)"/>
    <polygon points="270,6 420,6 420,18 268,18" fill="var(--green)"/>
    <polygon points="0,52 262,52 260,62 0,62" fill="var(--blue)"/>
  </svg>
</article>

<article class="card card-back">
  <div class="brand">
    <span class="brand-square"></span>
    <span class="brand-name">CraneHollow</span>
  </div>
</article>

</body>
</html>
```